Corvane Industries business cards

We need business cards for our company Corvane Industries, based in Brisbane but trading world wide. We buy and sell Corvane Industries, generators and marine equipment. The design needs to be kept clean, simple but eye catching.
Please keep with our current logo (included) and further information can be included on request

Business

0792cd
33a6d7
85cae6
3276b5
0455a3
cedeed
cee9f5
ffffff

```html
<!DOCTYPE html>
<html lang="en">
<head>
<meta charset="utf-8">
<title>Corvane Industries – Business Card</title>
<link href="https://fonts.googleapis.com/css2?family=Exo+2:wght@400;500;600&display=swap" rel="stylesheet">
<style>
  :root {
    --page: #e4e7eb;
    --card: #ffffff;
    --blue: #3f86c4;
    --blue-deep: #3276b5;
    --icon-blue: #0792cd;
    --ink: #1f2328;
    --rule: #3a3d42;
    --band-dark-1: #1e1f22;
    --band-dark-2: #4a4c50;
  }
  * { margin: 0; padding: 0; box-sizing: border-box; }
  html, body { width: 1200px; height: 817px; overflow: hidden; }
  body {
    background: var(--page);
    font-family: "Exo 2", "Segoe UI", sans-serif;
    position: relative;
  }
  .card {
    position: absolute;
    left: 100px; top: 118px;
    width: 1000px; height: 580px;
    background: var(--card);
    border-radius: 36px;
    overflow: hidden;
    box-shadow: 0 10px 30px rgba(0,0,0,.12);
  }
  .brand-band {
    position: absolute; left: 0; top: 150px;
    width: 100%; height: 52px;
    background: var(--blue);
  }
  .brand {
    position: absolute; left: 300px; top: 62px;
    width: 400px; height: 150px;
    background: var(--card);
    display: flex; align-items: center; gap: 22px;
    padding: 0 18px;
  }
  .brand-mark {
    width: 112px; height: 112px;
    background: var(--blue-deep);
    border-radius: 8px;
    flex: none;
  }
  .brand-name {
    color: var(--blue-deep);
    font-weight: 500;
    font-size: 46px;
    line-height: 0.98;
  }
  .brand-name small {
    display: block;
    font-size: 16px;
    text-align: right;
    margin-top: 4px;
  }
  .name-band {
    position: absolute; left: 0; top: 262px;
    width: 640px; height: 50px;
    background: var(--blue);
    display: flex; align-items: center;
    padding-left: 40px; gap: 18px;
    color: #fff;
  }
  .name-band svg { width: 34px; height: 34px; }
  .person-name { font-size: 30px; font-weight: 500; letter-spacing: 1px; }
  .divider { font-size: 28px; opacity: .9; }
  .person-title { font-size: 18px; letter-spacing: 1.5px; }
  .contacts {
    position: absolute; left: 0; top: 338px;
    width: 100%; height: 140px;
    display: flex;
  }
  .contact {
    flex: 1;
    display: flex; flex-direction: column; align-items: center;
    justify-content: space-between;
    padding: 6px 0 10px;
    color: var(--ink);
    font-size: 28px; font-weight: 500; letter-spacing: 1px;
  }
  .contact + .contact { border-left: 3px solid var(--rule); }
  .contact-icon {
    width: 74px; height: 74px; border-radius: 50%;
    background: var(--icon-blue);
    display: flex; align-items: center; justify-content: center;
  }
  .contact-icon svg { width: 40px; height: 40px; }
  .address-band {
    position: absolute; left: 0; top: 505px;
    width: 100%; height: 48px;
    background: linear-gradient(90deg, var(--band-dark-1), var(--band-dark-2) 60%, var(--band-dark-1));
    display: flex; align-items: center; gap: 16px;
    padding-left: 40px;
    color: #e6e6e6; font-size: 22px; letter-spacing: 2px;
  }
  .address-band svg { width: 22px; height: 30px; }
</style>
</head>
<body>
  <div class="card">
    <div class="brand-band"></div>
    <div class="brand">
      <div class="brand-mark"></div>
      <div class="brand-name">Corvane<br>Industries<small>Pty Ltd</small></div>
    </div>

    <div class="name-band">
      <svg viewBox="0 0 32 32" aria-hidden="true"><circle cx="16" cy="10" r="7" fill="#fff"/><path d="M3 31c0-8 6-12 13-12s13 4 13 12z" fill="#fff"/></svg>
      <span class="person-name">MARCUS HALE</span>
      <span class="divider">|</span>
      <span class="person-title">GENERAL MANAGER</span>
    </div>

    <div class="contacts">
      <div class="contact">
        <div class="contact-icon">
          <svg viewBox="0 0 40 40" aria-hidden="true"><rect x="12" y="4" width="16" height="32" rx="3" fill="none" stroke="#fff" stroke-width="2.5"/><line x1="12" y1="10" x2="28" y2="10" stroke="#fff" stroke-width="2"/><line x1="12" y1="30" x2="28" y2="30" stroke="#fff" stroke-width="2"/><circle cx="20" cy="33" r="1.4" fill="#fff"/></svg>
        </div>
        <span class="contact-text">012 555 0147</span>
      </div>
      <div class="contact">
        <div class="contact-icon">
          <svg viewBox="0 0 40 40" aria-hidden="true"><rect x="5" y="10" width="30" height="20" fill="#fff"/><path d="M5 10l15 12 15-12" fill="none" stroke="#0792cd" stroke-width="2"/></svg>
        </div>
        <span class="contact-text">info@corvane.com</span>
      </div>
      <div class="contact">
        <div class="contact-icon">
          <svg viewBox="0 0 40 40" aria-hidden="true" fill="none" stroke="#fff" stroke-width="2"><circle cx="20" cy="20" r="14"/><ellipse cx="20" cy="20" rx="6" ry="14"/><line x1="6" y1="20" x2="34" y2="20"/><line x1="20" y1="6" x2="20" y2="34"/><path d="M9 12h22M9 28h22"/></svg>
        </div>
        <span class="contact-text">www.corvaneind.com</span>
      </div>
    </div>

    <div class="address-band">
      <svg viewBox="0 0 22 30" aria-hidden="true"><path d="M11 1a10 10 0 0 0-10 10c0 8 10 18 10 18s10-10 10-18A10 10 0 0 0 11 1z" fill="#fff"/><circle cx="11" cy="11" r="4" fill="#2a2b2e"/></svg>
      <span class="address-text">041,9th floor,Harbour View Road QLD</span>
    </div>
  </div>
</body>
</html>
```